Business Card Design

We have a group of different function companies owned and operated by one person. We are located in the Dallas Fort Worth area in Texas. We develop properties to where we are owners and develop properties that are not ours as well. We build custom homes and commercial buildings. We also do residential and commercial remodeling. We also own commercial properties in which we lease office space. We are trying to merge all we do into one card and have done so already into one website. We initially had thought of having a logo made with HV in nice attractive lettering maybe as a watermark. We are open to the color scheme but no neons or pastels.

Project Deadline Extended
Reason: I am needing 2 different cards for two businesses.

Industry/Entity Type

Residential

Contact Information for Business Card

Harwell Ventures
4826 Mabry Ln. Suite 417
Keller, Texas 76109
Land Development
Residential and Commercial Construction
Commercial Real Estate
Dale Wintermoot
www.harwellgrp.example
dale@harwellgrp.example
Cell: 817-555-0142
Office: 817-555-0187
Fax: 8175550163

```html
<!DOCTYPE html>
<html lang="en">
<head>
<meta charset="utf-8">
<title>Harwell Ventures – Business Card</title>
<link href="https://fonts.googleapis.com/css2?family=Fira+Sans+Condensed:wght@400;600&display=swap" rel="stylesheet">
<style>
  :root {
    --teal: #17666a;
    --ink: #343b3d;
    --band: #8a9c9a;
    --ring: #c9d2d1;
    --bubble: #8fe3ea;
    --bg-light: #ffffff;
    --bg-mid: #eef1f1;
    --bg-edge: #d7dedd;
  }
  html, body {
    margin: 0;
    padding: 0;
    overflow: hidden;
    background: #ffffff;
  }
  .card {
    position: relative;
    width: 1200px;
    height: 702px;
    overflow: hidden;
    background:
      radial-gradient(ellipse 420px 260px at 140px 240px, var(--bg-light) 0%, rgba(255,255,255,0) 100%),
      radial-gradient(ellipse 900px 600px at 50% 45%, var(--bg-mid) 0%, var(--bg-edge) 100%);
    font-family: "Fira Sans Condensed", "Arial Narrow", sans-serif;
    color: var(--ink);
  }
  .card-art {
    position: absolute;
    inset: 0;
  }
  .company-name {
    position: absolute;
    top: 92px;
    left: 0;
    width: 1200px;
    margin: 0;
    text-align: center;
    font-weight: 600;
    font-size: 70px;
    letter-spacing: 1px;
    color: var(--teal);
  }
  .person {
    position: absolute;
    left: 69px;
    top: 480px;
    margin: 0;
    font-weight: 600;
    font-size: 42px;
    line-height: 1;
    color: var(--ink);
  }
  .person .surname { color: var(--teal); }
  .role {
    position: absolute;
    left: 156px;
    top: 537px;
    font-weight: 600;
    font-size: 17px;
    color: var(--ink);
  }
  .email {
    position: absolute;
    left: 70px;
    top: 569px;
    display: flex;
    align-items: center;
    gap: 8px;
    font-size: 25px;
    color: var(--ink);
  }
  .address {
    position: absolute;
    left: 0;
    width: 1130px;
    top: 614px;
    text-align: center;
    font-size: 25px;
    color: var(--ink);
  }
  .phones {
    position: absolute;
    left: 911px;
    top: 438px;
    margin: 0;
    font-size: 25px;
    line-height: 38px;
    color: var(--ink);
  }
  .phones .row { display: flex; }
  .phones dt { width: 77px; margin: 0; }
  .phones dd { margin: 0; }
  .website {
    position: absolute;
    left: 871px;
    top: 564px;
    display: flex;
    align-items: center;
    gap: 12px;
    font-size: 25px;
    color: var(--ink);
  }
</style>
</head>
<body>
  <div class="card">
    <svg class="card-art" width="1200" height="702" viewBox="0 0 1200 702" aria-hidden="true">
      <rect class="band" x="0" y="323" width="1200" height="82" fill="var(--band)"/>
      <rect class="band-stripe" x="0" y="357" width="1200" height="11" fill="var(--teal)"/>
      <circle class="bubble" cx="708" cy="290" r="50" fill="var(--bubble)" opacity="0.7"/>
      <circle class="bubble" cx="652" cy="265" r="28" fill="var(--bubble)" opacity="0.45"/>
      <circle class="bubble" cx="470" cy="424" r="53" fill="var(--bubble)" opacity="0.65"/>
      <circle class="bubble" cx="523" cy="462" r="27" fill="var(--bubble)" opacity="0.45"/>
      <circle class="emblem-ring" cx="583" cy="354" r="122" fill="var(--ring)" opacity="0.9"/>
      <circle class="emblem" cx="583" cy="354" r="112" fill="var(--teal)"/>
    </svg>

    <h1 class="company-name">Harwell Ventures</h1>

    <h2 class="person">Dale <span class="surname">Wintermoot</span></h2>
    <div class="role">President</div>

    <div class="email">
      <svg width="24" height="17" viewBox="0 0 24 17" aria-hidden="true">
        <rect x="1" y="1" width="22" height="15" fill="none" stroke="var(--teal)" stroke-width="2"/>
        <path d="M1 1 L12 10 L23 1" fill="none" stroke="var(--teal)" stroke-width="2"/>
      </svg>
      <span>dale@harwellgrp.example</span>
    </div>

    <dl class="phones">
      <div class="row"><dt>Cell:</dt><dd>817-555-0142</dd></div>
      <div class="row"><dt>Office:</dt><dd>817-555-0176</dd></div>
      <div class="row"><dt>Fax:</dt><dd>817-555-0163</dd></div>
    </dl>

    <div class="website">
      <svg width="24" height="24" viewBox="0 0 24 24" aria-hidden="true">
        <g fill="none" stroke="var(--teal)" stroke-width="1.8">
          <circle cx="12" cy="12" r="10"/>
          <ellipse cx="12" cy="12" rx="4.5" ry="10"/>
          <line x1="2" y1="12" x2="22" y2="12"/>
          <line x1="3.5" y1="7" x2="20.5" y2="7"/>
          <line x1="3.5" y1="17" x2="20.5" y2="17"/>
        </g>
      </svg>
      <span>www.harwellgrp.example</span>
    </div>

    <div class="address">4826 Mabry Ln. Suite 417 Keller, Texas 76109</div>
  </div>
</body>
</html>
```